Business card design needed

We are a smash repair business and have been in operation for almost 10 years. We have always had a card with a solid yellow background and black car door as a logo. We don't want to stray too far from this as all of our advertising incorporates same.

We do not wish to have anything comical or too wordy.

Industry/Entity Type

Advertising

Contact Information for Business Card

Rhys & Gemma Tolland
Brookvale Ridge Panel Works
Bays 7-11 Wexford Crescent
Harwood Bay NSW 2446
02 6571 3820
0428 362 057
office@brookvaleridgepanelworks.com.au

Logo Text

Brookvale Ridge Panel Works

Logo styles of interest
Emblem Logo

```html
<!DOCTYPE html>
<html lang="en">
<head>
<meta charset="utf-8">
<title>Brookvale Ridge Panel Works – Business Card</title>
<link rel="stylesheet" href="https://fonts.googleapis.com/css2?family=Roboto+Condensed:wght@700&display=swap">
<style>
  :root {
    --backdrop: #6a3226;
    --card-white: #ffffff;
    --card-grey: #d9d9d9;
    --brand-yellow: #fff200;
    --ink: #111111;
    --shadow: rgba(0, 0, 0, 0.45);
  }
  * { box-sizing: border-box; margin: 0; padding: 0; }
  html, body {
    width: 1200px;
    height: 867px;
    overflow: hidden;
    background: var(--backdrop);
    font-family: "Roboto Condensed", "Arial Narrow", sans-serif;
    font-weight: 700;
    color: var(--ink);
  }
  .canvas { position: relative; width: 1200px; height: 867px; }

  .card {
    position: absolute;
    width: 640px;
    height: 390px;
    border-radius: 18px;
    overflow: hidden;
    box-shadow: 0 14px 30px var(--shadow);
  }

  /* Front */
  .card-front {
    left: 60px;
    top: 40px;
    background: linear-gradient(100deg, var(--card-grey) 0%, var(--card-white) 12%, var(--card-white) 85%, var(--card-grey) 100%);
  }
  .hazard-band {
    position: absolute;
    left: 0;
    width: 100%;
    height: 30px;
    background: var(--ink);
  }
  .hazard-band.top { top: 0; }
  .hazard-band.bottom { bottom: 0; }
  .front-brand {
    position: absolute;
    left: 0;
    right: 0;
    top: 150px;
    display: flex;
    align-items: center;
    justify-content: center;
    gap: 18px;
  }
  .brand-square {
    width: 62px;
    height: 62px;
    background: var(--ink);
    flex: none;
  }
  .brand-name {
    font-size: 40px;
    line-height: 1.0;
    color: var(--ink);
  }

  /* Back */
  .card-back {
    left: 500px;
    top: 430px;
    background: var(--brand-yellow);
  }
  .back-logo-side {
    position: absolute;
    left: 0;
    top: 0;
    width: 330px;
    height: 100%;
    background: linear-gradient(90deg, var(--card-white) 0%, var(--card-white) 78%, var(--card-grey) 100%);
    display: flex;
    flex-direction: column;
    align-items: center;
    justify-content: center;
    gap: 16px;
    text-align: center;
  }
  .back-logo-side .brand-name { font-size: 36px; }
  .divider {
    position: absolute;
    top: 0;
    height: 100%;
    background: var(--ink);
  }
  .divider.thick { left: 332px; width: 7px; }
  .divider.thin { left: 343px; width: 2px; }

  .contact {
    position: absolute;
    left: 370px;
    top: 62px;
    right: 14px;
  }
  .contact-names { font-size: 26px; margin-bottom: 30px; padding-left: 4px; }
  .contact-group { margin-bottom: 16px; }
  .contact-row {
    display: flex;
    align-items: flex-start;
    gap: 10px;
    font-size: 14.5px;
    line-height: 1.3;
  }
  .contact-row svg { width: 12px; height: 12px; flex: none; margin-top: 3px; }
  .contact-row.small { font-size: 13.5px; }
</style>
</head>
<body>
<main class="canvas">

  <section class="card card-front" aria-label="Business card front">
    <div class="hazard-band top" role="img" aria-label="Yellow and black hazard stripe band"></div>
    <div class="front-brand">
      <span class="brand-square"></span>
      <span class="brand-name">Brookvale Ridge<br>Panel Works</span>
    </div>
    <div class="hazard-band bottom" role="img" aria-label="Yellow and black hazard stripe band"></div>
  </section>

  <section class="card card-back" aria-label="Business card back">
    <div class="back-logo-side">
      <span class="brand-square"></span>
      <span class="brand-name">Brookvale Ridge<br>Panel Works</span>
    </div>
    <span class="divider thick"></span>
    <span class="divider thin"></span>

    <div class="contact">
      <p class="contact-names">Rhys &amp; Gemma Tolland</p>

      <div class="contact-group">
        <p class="contact-row">
          <svg viewBox="0 0 12 12" aria-hidden="true"><path d="M6 0.5a4 4 0 0 1 4 4c0 3-4 7-4 7s-4-4-4-7a4 4 0 0 1 4-4z" fill="#111"/><circle cx="6" cy="4.5" r="1.5" fill="#fff200"/></svg>
          <span>Bays 7-11<br>Wexford Crescent<br>Harwood Bay NSW 2446</span>
        </p>
      </div>

      <div class="contact-group">
        <p class="contact-row">
          <svg viewBox="0 0 12 12" aria-hidden="true"><path d="M2 1l2.2 0 1 2.6-1.3 1a6.5 6.5 0 0 0 3.5 3.5l1-1.3 2.6 1V11A1 1 0 0 1 10 12 10 10 0 0 1 0 2a1 1 0 0 1 1-1z" fill="#111"/></svg>
          <span>02 6571 3820</span>
        </p>
        <p class="contact-row">
          <svg viewBox="0 0 12 12" aria-hidden="true"><rect x="3" y="0.5" width="6" height="11" rx="1" fill="#111"/><rect x="4" y="2" width="4" height="7" fill="#fff200"/></svg>
          <span>0428 362 057</span>
        </p>
      </div>

      <div class="contact-group">
        <p class="contact-row small">
          <svg viewBox="0 0 12 12" aria-hidden="true"><rect x="0.5" y="2.5" width="11" height="7" fill="#111"/><path d="M0.5 2.5l5.5 4 5.5-4" stroke="#fff200" stroke-width="1" fill="none"/></svg>
          <span>office@brookvaleridgepanelworks.com.au</span>
        </p>
        <p class="contact-row small">
          <svg viewBox="0 0 12 12" aria-hidden="true"><circle cx="6" cy="6" r="5.2" fill="#111"/><path d="M1 6h10M6 1c-2.5 3-2.5 7 0 10M6 1c2.5 3 2.5 7 0 10" stroke="#fff200" stroke-width="0.8" fill="none"/></svg>
          <span>www.brookvaleridgepanelworks.com.au</span>
        </p>
      </div>
    </div>
  </section>

</main>
</body>
</html>
```